Roofing Company needs YOU to help put us on top!

Brightpeak Roofing, a fresh new company with quality and Innovation in mind, needs your help to stand out in the competitive Chicago market. With over 30 years of experience, all the right people and tools for the job, the only thing we are missing is your creative ideas in web design to help us grow our online presence.
Our Company offers exceptional quality at reasonable prices, we work for the everyday people both blue collar and white collar.

We have used Craftswarm in the past with multiple successful campaigns, we are excited to see what you can come up with for our website.

www.BrightpeakRoofing.example will be the domain

We will be hiring a photographer for visual content on our pages later. Stock photos are okay to use but should follow theme.

Thank you for taking the time on the submissions, if you have any questions don't hesitate to ask and we will provide whatever is needed to you.

Target Market(s)

Homeowners & Commercial Clients between 21-65

Industry/Entity Type

Roofing

Coding

Coded - Design and coding required

Number of Pages Required

4 page

Font styles to use
Sans Serif

Colors
ffffff
ec1f27
000000
5c5c5c
757575
b2b2b2

Requirements
Must have
• Color Scheme - should follow around our logo
• As for pages we were looking for an About, Services, Projects (gallery page) and Contact.
• Main page please include social media links and a a place so people could use tillbee to make payments
• Website should work on desktop as well as mobile platforms
Nice to have
• A Live chat feature would be nice if possible
Should not have
• Obscure Colors or Common web templates

```html
<!DOCTYPE html>
<html lang="en">
<head>
<meta charset="utf-8">
<title>Contact – Brightpeak Roofing</title>
<link rel="stylesheet" href="https://fonts.googleapis.com/css2?family=Roboto:wght@400;500;700&family=Open+Sans:wght@400;600&display=swap">
<style>
  :root{
    --red:#ec1f27;
    --black:#000000;
    --ink:#222222;
    --grey-dark:#5c5c5c;
    --grey:#757575;
    --grey-light:#b2b2b2;
    --white:#ffffff;
    --footer:#1e1e1e;
    --line:#bdbdbd;
  }
  *{box-sizing:border-box;margin:0;padding:0}
  html,body{width:1172px;height:1200px;overflow:hidden;background:var(--white)}
  body{position:relative;font-family:"Roboto",sans-serif;color:var(--ink)}
  .abs{position:absolute}
  a{color:inherit;text-decoration:none}

  /* top bar */
  .topbar{left:0;top:0;width:1172px;height:42px;background:var(--black);color:var(--white);font-size:11px;font-weight:500}
  .social{display:flex;gap:10px;align-items:center}
  .social span{font-size:10.5px;font-weight:500}
  .topbar .social{left:87px;top:14px}
  .top-contacts{right:87px;top:14px;display:flex;gap:14px;align-items:center}
  .top-contacts .item{display:flex;align-items:center;gap:6px}

  /* nav */
  .brand{left:86px;top:62px;display:flex;align-items:center;gap:7px;font-weight:700;font-size:18px;color:var(--ink)}
  .brand .mark{width:14px;height:14px;background:var(--red)}
  .nav{top:66px;left:0;width:1172px;font-size:13px;color:var(--ink)}
  .nav a{position:absolute}
  .nav .active{color:var(--red)}
  .nav-underline{left:777px;top:92px;width:55px;height:2px;background:var(--red)}

  /* banner */
  .banner{left:0;top:114px;width:1172px;height:88px;background:linear-gradient(100deg,#3a4450 0%,#2a3440 45%,#1d2733 70%,#303a46 100%)}
  .banner h1{position:absolute;left:87px;top:30px;font-family:"Open Sans",sans-serif;font-weight:400;font-size:24px;color:var(--white)}
  .banner .crumb{position:absolute;right:87px;top:37px;font-size:12.5px;color:var(--white);font-family:"Open Sans",sans-serif}

  /* contact info */
  .info{font-family:"Open Sans",sans-serif}
  .info h2{position:absolute;left:94px;top:304px;font-weight:400;font-size:17px;color:var(--ink);font-family:"Roboto",sans-serif}
  .info .label{position:absolute;display:flex;align-items:center;gap:8px;font-size:13.5px;color:var(--ink)}
  .info .value{position:absolute;font-size:12.5px;color:var(--grey)}
  .btn-call{left:86px;top:531px;width:118px;height:39px;border-radius:20px;background:var(--red);color:var(--white);font-size:11px;font-weight:700;display:flex;align-items:center;justify-content:center;letter-spacing:.3px}

  /* form card */
  .card{left:398px;top:273px;width:670px;height:318px;background:var(--white);box-shadow:0 2px 14px rgba(0,0,0,.09)}
  .card h2{position:absolute;left:50px;top:37px;font-size:17px;font-weight:400;color:var(--ink)}
  .field{position:absolute;border-bottom:1px solid var(--line);font-family:"Open Sans",sans-serif;font-size:11.5px;color:var(--grey);padding:0 3px 18px}
  .send{position:absolute;left:48px;top:261px;font-family:"Open Sans",sans-serif;font-size:11.5px;font-weight:600;color:var(--ink);letter-spacing:.3px;padding-bottom:6px;border-bottom:2px solid var(--ink)}
  .mail-fab{left:1041px;top:307px;width:46px;height:46px;border-radius:50%;background:var(--red);box-shadow:0 3px 8px rgba(0,0,0,.25);display:flex;align-items:center;justify-content:center}

  /* map */
  .map{left:0;top:653px;width:1172px;height:294px;background:linear-gradient(160deg,#e9e9e9 0%,#dcdcdc 50%,#e6e6e6 100%)}
  .live-chat{left:897px;top:919px;width:275px;height:28px;background:#f1f1f1;display:flex}
  .live-chat .toggle{width:30px;height:28px;background:var(--footer);display:flex;align-items:center;justify-content:center}
  .live-chat .title{padding-left:14px;line-height:28px;font-size:12px;font-weight:500;color:var(--ink)}

  /* footer */
  .footer{left:0;top:947px;width:1172px;height:213px;background:var(--footer);color:var(--white)}
  .footer h3{position:absolute;top:32px;font-size:16px;font-weight:500}
  .footer p,.footer li{font-size:11.5px;line-height:17.4px;color:#e6e6e6}
  .footer .about{position:absolute;left:88px;top:64px;width:270px}
  .footer ul{position:absolute;left:422px;top:58px;list-style:none;font-family:"Open Sans",sans-serif}
  .footer ul li{height:23.4px}
  .footer .follow{position:absolute;left:604px;top:63px;width:220px}
  .newsletter{position:absolute;left:604px;top:112px;width:208px;height:16px;border-bottom:1px solid #6a6a6a;font-size:11px;color:#9a9a9a;padding-left:6px}
  .newsletter svg{position:absolute;right:10px;top:0}
  .contact-list{position:absolute;left:890px;top:63px;width:200px;font-size:11.5px;color:#e6e6e6}
  .contact-list .row{position:absolute;left:0;display:flex;gap:10px;line-height:17.4px;width:200px}
  .contact-list svg{flex:none;margin-top:4px}

  .bottom{left:0;top:1160px;width:1172px;height:40px;background:var(--black);color:var(--white)}
  .bottom .copy{position:absolute;left:89px;top:13px;font-size:11.5px;font-family:"Open Sans",sans-serif}
  .bottom .social{position:absolute;right:86px;top:14px}
</style>
</head>
<body>

<header class="abs topbar">
  <div class="abs social">
    <span>Loop</span><span>Pica</span><span>Vox</span><span>Nexa</span>
  </div>
  <div class="abs top-contacts">
    <div class="item">
      <svg width="12" height="9" viewBox="0 0 12 9" fill="none" stroke="#fff"><rect x=".5" y=".5" width="11" height="8"/><path d="M.5 .5 6 5l5.5-4.5"/></svg>
      hello@brightpeak.example
    </div>
    <div class="item">
      <svg width="11" height="11" viewBox="0 0 24 24" fill="none" stroke="#fff" stroke-width="2"><path d="M22 16.9v3a2 2 0 0 1-2.2 2 19.8 19.8 0 0 1-8.6-3.1 19.5 19.5 0 0 1-6-6A19.8 19.8 0 0 1 2.1 4.2 2 2 0 0 1 4.1 2h3a2 2 0 0 1 2 1.7c.1 1 .4 1.9.7 2.8a2 2 0 0 1-.5 2.1L8 9.8a16 16 0 0 0 6 6l1.3-1.3a2 2 0 0 1 2.1-.4c.9.3 1.8.6 2.8.7a2 2 0 0 1 1.7 2z"/></svg>
      312-555-0148
    </div>
    <div class="item">
      <svg width="10" height="12" viewBox="0 0 10 12" fill="none" stroke="#fff"><path d="M5 11.5S9.5 7 9.5 4.5a4.5 4.5 0 0 0-9 0C.5 7 5 11.5 5 11.5z"/><circle cx="5" cy="4.5" r="1.6"/></svg>
      Locations
    </div>
  </div>
</header>

<a class="abs brand" href="#"><span class="mark"></span>Brightpeak Roofing</a>

<nav class="abs nav">
  <a class="active" style="left:788px">Home</a>
  <a style="left:846px">About</a>
  <a style="left:905px">Service</a>
  <a style="left:971px">Projects</a>
  <a style="left:1042px">Contact</a>
</nav>
<div class="abs nav-underline"></div>

<section class="abs banner" role="img" aria-label="Dark photo of a modern building facade">
  <h1>Contact</h1>
  <div class="crumb">Home / Contact</div>
</section>

<section class="info">
  <h2>CONTACT INFO</h2>
  <div class="label" style="left:94px;top:343px">
    <svg width="12" height="14" viewBox="0 0 10 12" fill="none" stroke="#333"><path d="M5 11.5S9.5 7 9.5 4.5a4.5 4.5 0 0 0-9 0C.5 7 5 11.5 5 11.5z"/><circle cx="5" cy="4.5" r="1.6"/></svg>
    Address
  </div>
  <div class="value" style="left:95px;top:369px">Head Office: 48 Ridgeline Avenue Chicago</div>
  <div class="label" style="left:91px;top:410px">
    <svg width="12" height="12" viewBox="0 0 24 24" fill="none" stroke="#333" stroke-width="2"><path d="M22 16.9v3a2 2 0 0 1-2.2 2 19.8 19.8 0 0 1-8.6-3.1 19.5 19.5 0 0 1-6-6A19.8 19.8 0 0 1 2.1 4.2 2 2 0 0 1 4.1 2h3a2 2 0 0 1 2 1.7c.1 1 .4 1.9.7 2.8a2 2 0 0 1-.5 2.1L8 9.8a16 16 0 0 0 6 6l1.3-1.3a2 2 0 0 1 2.1-.4c.9.3 1.8.6 2.8.7a2 2 0 0 1 1.7 2z"/></svg>
    Phone
  </div>
  <div class="value" style="left:91px;top:436px">312-555-0148</div>
  <div class="label" style="left:92px;top:474px">
    <svg width="12" height="9" viewBox="0 0 12 9" fill="none" stroke="#333"><rect x=".5" y=".5" width="11" height="8"/><path d="M.5 .5 6 5l5.5-4.5"/></svg>
    EMAIL
  </div>
  <div class="value" style="left:91px;top:500px">hello@brightpeak.example</div>
  <a class="abs btn-call" href="#">CALL US</a>
</section>

<form class="abs card">
  <h2>CONTACT US</h2>
  <div class="field" style="left:50px;top:77px;width:257px">First Name*</div>
  <div class="field" style="left:340px;top:77px;width:258px">Second Name*</div>
  <div class="field" style="left:50px;top:130px;width:257px">Your Email*</div>
  <div class="field" style="left:340px;top:130px;width:258px">Subject</div>
  <div class="field" style="left:49px;top:182px;width:549px;height:55px;padding-left:6px">Message*</div>
  <div class="send">SEND MESSAGE</div>
</form>
<div class="abs mail-fab">
  <svg width="18" height="13" viewBox="0 0 12 9" fill="none" stroke="#fff" stroke-width=".9"><rect x=".5" y=".5" width="11" height="8"/><path d="M.5 .5 6 5l5.5-4.5M.5 8.5 4.5 4.2M11.5 8.5 7.5 4.2"/></svg>
</div>

<section class="abs map" role="img" aria-label="Street map showing the office location"></section>
<div class="abs live-chat">
  <div class="toggle"><svg width="10" height="6" viewBox="0 0 10 6" fill="none" stroke="#fff" stroke-width="1.6"><path d="M1 5 5 1l4 4"/></svg></div>
  <div class="title">Live Chat</div>
</div>

<footer class="abs footer">
  <h3 style="left:88px">About</h3>
  <p class="about">Aenean vulputate eleifend tellus aenean leo ligula porttitor eu consequat vitae eleifend ac enim aliquam lorem ante dapibus in viverra quis feugiat a tellus phasellus viverra nulla ut metus varius laoreet quis-que rutrum.</p>

  <h3 style="left:422px">Useful Links</h3>
  <ul>
    <li>Steelform Roofing</li>
    <li>Repairs &amp; Maintenance</li>
    <li>Whirlybird Installation</li>
    <li>Leaf Free Gutter Guard</li>
    <li>Gutters, Downpipes</li>
  </ul>

  <h3 style="left:604px">Follow Us</h3>
  <p class="follow">Subscribe to our newsletter to get latest updates and offers.</p>
  <div class="newsletter">Enter email
    <svg width="13" height="11" viewBox="0 0 13 11" fill="var(--red)"><path d="M0 5 13 0 10 11 6 7 11 2 4 6z"/></svg>
  </div>

  <h3 style="left:890px">Contact information</h3>
  <div class="contact-list">
    <div class="row" style="top:0">
      <svg width="8" height="10" viewBox="0 0 10 12" fill="#ddd"><path d="M5 12S10 7 10 4.5a5 5 0 0 0-10 0C0 7 5 12 5 12z"/></svg>
      <span>Some address line here..., area info, City name, Country name.</span>
    </div>
    <div class="row" style="top:43px">
      <svg width="9" height="9" viewBox="0 0 24 24" fill="#ddd"><path d="M22 16.9v3a2 2 0 0 1-2.2 2 19.8 19.8 0 0 1-8.6-3.1 19.5 19.5 0 0 1-6-6A19.8 19.8 0 0 1 2.1 4.2 2 2 0 0 1 4.1 2h3a2 2 0 0 1 2 1.7c.1 1 .4 1.9.7 2.8a2 2 0 0 1-.5 2.1L8 9.8a16 16 0 0 0 6 6l1.3-1.3a2 2 0 0 1 2.1-.4c.9.3 1.8.6 2.8.7a2 2 0 0 1 1.7 2z"/></svg>
      <span>312-555-0148</span>
    </div>
    <div class="row" style="top:69px">
      <svg width="9" height="7" viewBox="0 0 12 9" fill="#ddd"><rect width="12" height="9"/></svg>
      <span>hello@brightpeak.example</span>
    </div>
  </div>
</footer>

<div class="abs bottom">
  <div class="copy">Copyright 2016. All Right Reserved</div>
  <div class="social">
    <span>Loop</span><span>Pica</span><span>Vox</span><span>Nexa</span>
  </div>
</div>

</body>
</html>
```